Outdoor cooking competition needs 10yr celebration poster

We are a fundraising event held every year in a tiny outback town in australia. the cooking competition is a 'camp oven' themed competition. people are required to cook in the ground in coals with a camp oven (dutch oven).
the event is celebrating ten years and needs a new flashy poster to let people know.

the event raises much needed funds for "the Silver Wing Medics" a a donation funded scheme which flys doctors and patients to and from remote australia.

The EMBER RIDGE FEAST is held annually in the tiny town of Blinman in the northern Flinders Ranges. The main street of the town, camp ground, and surrounding area have been landscaped to suit the competitions purpose. A giant ‘creek bed’ kitchen is created with tones of rocks and gravel transforming the street and adjacent hill side. The picturesque and historic Tarrock Hotel with its verandahs and characteristic front bar, will form a focus, the remaining street precinct will be the venue for exhibitions, wine tasting, food outlets, trade displays, demonstrations and live music.

• Must display our logo
dates and venues
10 year celebration
room to add sponsorship logos

```html
<!DOCTYPE html>
<html lang="en">
<head>
<meta charset="utf-8">
<title>Ember Ridge Feast – Celebrating 10 Years</title>
<link rel="stylesheet" href="https://fonts.googleapis.com/css2?family=Oswald:wght@500;600;700&family=Antonio:wght@300;400&family=Rye&family=Archivo+Black&display=swap">
<style>
  :root {
    --paper-light: #f0ede5;
    --paper-dark: #e2ddd0;
    --ink-black: #141210;
    --rust: #a8692c;
    --brown: #6e3c1f;
    --saddle: #5b2e14;
    --pot-iron: #1c1917;
    --fire-tone: #c9955a;
  }
  html, body {
    margin: 0;
    padding: 0;
    width: 900px;
    height: 1200px;
    overflow: hidden;
    background: var(--paper-light);
  }
  .poster {
    display: block;
    width: 900px;
    height: 1200px;
  }
  .paper { fill: url(#paperTone); }
  .brand-name {
    font-family: "Oswald", "Arial Narrow", sans-serif;
    font-weight: 700;
    fill: var(--ink-black);
  }
  .headline {
    font-family: "Oswald", "Arial Narrow", sans-serif;
    font-weight: 600;
    fill: var(--rust);
  }
  .event-dates {
    font-family: "Antonio", "Arial Narrow", sans-serif;
    font-weight: 300;
    fill: var(--brown);
  }
  .event-title {
    font-family: "Oswald", "Arial Narrow", sans-serif;
    font-weight: 500;
    fill: var(--rust);
  }
  .event-subtitle {
    font-family: "Oswald", "Arial Narrow", sans-serif;
    font-weight: 600;
    fill: var(--brown);
  }
  .venue,
  .tagline-western {
    font-family: "Rye", Georgia, serif;
    fill: var(--saddle);
  }
  .tagline-bold {
    font-family: "Archivo Black", "Arial Black", sans-serif;
    fill: var(--brown);
  }
  .tagline-light {
    font-family: "Antonio", "Arial Narrow", sans-serif;
    font-weight: 400;
    fill: var(--rust);
  }
  .tagline-tall {
    font-family: "Oswald", "Arial Narrow", sans-serif;
    font-weight: 500;
    fill: var(--rust);
  }
  .camp-oven-art { fill: var(--pot-iron); }
  .campfire-art { fill: url(#fireTone); }
</style>
</head>
<body>
<svg class="poster" viewBox="0 0 900 1200" xmlns="http://www.w3.org/2000/svg">
  <defs>
    <radialGradient id="paperTone" cx="50%" cy="45%" r="75%">
      <stop offset="0" stop-color="#f2efe8"/>
      <stop offset="1" stop-color="#e0dbce"/>
    </radialGradient>
    <linearGradient id="fireTone" x1="0" y1="0" x2="0" y2="1">
      <stop offset="0" stop-color="#d8b07c"/>
      <stop offset="1" stop-color="#9c6a3a"/>
    </linearGradient>
  </defs>

  <rect class="paper" width="900" height="1200"/>

  <g class="brand-block">
    <text class="brand-name" x="40" y="148" font-size="140" textLength="320" lengthAdjust="spacingAndGlyphs">EMBER</text>
    <text class="brand-name" x="40" y="278" font-size="140" textLength="320" lengthAdjust="spacingAndGlyphs">RIDGE</text>
    <text class="brand-name" x="40" y="408" font-size="140" textLength="320" lengthAdjust="spacingAndGlyphs">FEAST</text>
  </g>

  <g class="anniversary">
    <text class="headline" x="390" y="100" font-size="98" textLength="500" lengthAdjust="spacingAndGlyphs">CELEBRATING</text>
    <text class="headline" x="390" y="222" font-size="142" textLength="498" lengthAdjust="spacingAndGlyphs">10 YEARS</text>
    <text class="event-dates" x="390" y="408" font-size="220" textLength="495" lengthAdjust="spacingAndGlyphs">SEPTEMBER 29-30, 2012</text>
  </g>

  <g class="competition">
    <text class="event-title" x="32" y="612" font-size="220" textLength="470" lengthAdjust="spacingAndGlyphs">CAMP OVEN</text>
    <text class="event-subtitle" x="520" y="522" font-size="100" textLength="160" lengthAdjust="spacingAndGlyphs">COOK</text>
    <text class="event-subtitle" x="520" y="612" font-size="100" textLength="135" lengthAdjust="spacingAndGlyphs">OFF</text>
    <rect class="camp-oven-art" x="705" y="440" width="190" height="192" rx="30" role="img" aria-label="Illustration of a black cast-iron camp oven with a wire handle"/>
  </g>

  <text class="venue" x="28" y="728" font-size="82" textLength="862" lengthAdjust="spacingAndGlyphs">TARROCK  HOTEL</text>

  <g class="tagline">
    <text class="tagline-bold" x="30" y="802" font-size="58" textLength="345" lengthAdjust="spacingAndGlyphs">IS THAT A</text>
    <text class="tagline-tall" x="378" y="900" font-size="200" textLength="508" lengthAdjust="spacingAndGlyphs">JUMBUCK</text>
    <text class="tagline-light" x="185" y="890" font-size="64" textLength="180" lengthAdjust="spacingAndGlyphs">IN YOUR</text>
    <rect class="campfire-art" x="35" y="835" width="140" height="185" rx="10" role="img" aria-label="Sketch of a campfire with flames over crossed logs"/>
    <text class="tagline-western" x="210" y="1005" font-size="96" textLength="680" lengthAdjust="spacingAndGlyphs">TUCKERBAG?</text>
  </g>
</svg>
</body>
</html>
```